Fenmoor Business Card

I want a business card for me and my employees.
On one side it must be in Greek and on the other side in English. The color must much the one of the logo

Target Market(s)

Customers that are looking for security and antipiracy advisors

Contact Information for Business Card

Title, Email, Phone, website , Mobile Address Zip code, city and country

Requirements
Must have
• The colors of our logo (the blue ones)

```html
<!DOCTYPE html>
<html lang="en">
<head>
<meta charset="utf-8">
<title>Fenmoor Advisory – Business Cards</title>
<link href="https://fonts.googleapis.com/css2?family=Montserrat:wght@400;600;700&display=swap" rel="stylesheet">
<style>
  :root {
    --navy: #262356;
    --ink: #3d3d45;
    --card: #ffffff;
    --backdrop: #e6e7ea;
  }
  * { box-sizing: border-box; margin: 0; padding: 0; }
  html, body { width: 1200px; height: 900px; overflow: hidden; }
  body {
    background: var(--backdrop);
    font-family: "Montserrat", Arial, sans-serif;
    position: relative;
  }
  .card {
    position: absolute;
    left: 290px;
    width: 620px;
    height: 354px;
    background: var(--card);
    border-radius: 34px;
    box-shadow: 0 6px 18px rgba(0,0,0,0.12);
  }
  .card--english { top: 78px; }
  .card--greek { top: 468px; }

  .holder {
    position: absolute;
    left: 40px;
    top: 40px;
  }
  .holder__name {
    font-size: 17px;
    font-weight: 700;
    color: var(--navy);
    letter-spacing: 0.3px;
  }
  .holder__role {
    font-weight: 400;
    color: var(--ink);
    font-size: 15px;
  }
  .holder__divider { color: var(--navy); font-weight: 700; margin: 0 4px; }
  .holder__mobile {
    margin-top: 8px;
    display: flex;
    align-items: center;
    gap: 8px;
    font-size: 15px;
    color: var(--ink);
  }

  .brand {
    position: absolute;
    left: 50%;
    top: 150px;
    transform: translateX(-50%);
    display: flex;
    align-items: center;
    gap: 14px;
    white-space: nowrap;
  }
  .brand__square {
    width: 34px;
    height: 34px;
    background: var(--navy);
  }
  .brand__name {
    font-size: 38px;
    font-weight: 700;
    color: var(--navy);
    letter-spacing: 1px;
    text-transform: uppercase;
  }

  .contact {
    position: absolute;
    right: 36px;
    bottom: 34px;
    list-style: none;
    text-align: right;
  }
  .contact__item {
    display: flex;
    justify-content: flex-end;
    align-items: center;
    gap: 9px;
    font-size: 14px;
    color: var(--ink);
    line-height: 25px;
  }
  .contact__item svg { width: 14px; height: 14px; fill: var(--navy); flex: none; }
</style>
</head>
<body>

<article class="card card--english" lang="en">
  <div class="holder">
    <p class="holder__name">JOHN SMITH<span class="holder__divider">|</span><span class="holder__role">Director</span></p>
    <p class="holder__mobile">
      <svg width="10" height="16" viewBox="0 0 10 16"><rect x="1" y="1" width="8" height="14" rx="1.5" fill="none" stroke="var(--navy)" stroke-width="1.5"/><rect x="3.5" y="12" width="3" height="1.2" fill="var(--navy)"/></svg>
      300-200-9000
    </p>
  </div>
  <div class="brand">
    <span class="brand__square"></span>
    <span class="brand__name">Fenmoor Advisory</span>
  </div>
  <ul class="contact">
    <li class="contact__item">300-200-9000 <svg viewBox="0 0 24 24"><path d="M6.6 10.8a15.1 15.1 0 0 0 6.6 6.6l2.2-2.2c.3-.3.7-.4 1-.2 1.1.4 2.3.6 3.6.6.6 0 1 .4 1 1V20c0 .6-.4 1-1 1A17 17 0 0 1 3 4c0-.6.4-1 1-1h3.5c.6 0 1 .4 1 1 0 1.3.2 2.5.6 3.6.1.3 0 .7-.2 1z"/></svg></li>
    <li class="contact__item">info@fenmooradvisory.com <svg viewBox="0 0 24 24"><path d="M2 5h20v14H2z" fill="var(--navy)"/><path d="M2 5l10 8 10-8" fill="none" stroke="#fff" stroke-width="1.6"/></svg></li>
    <li class="contact__item">www.fenmooradvisory.com <svg viewBox="0 0 24 24"><circle cx="12" cy="12" r="10" fill="none" stroke="var(--navy)" stroke-width="1.8"/><ellipse cx="12" cy="12" rx="4" ry="10" fill="none" stroke="var(--navy)" stroke-width="1.5"/><path d="M2 12h20M4 7h16M4 17h16" stroke="var(--navy)" stroke-width="1.3"/></svg></li>
    <li class="contact__item">00 dummy city, place 0000 <svg viewBox="0 0 24 24"><path d="M12 2a7 7 0 0 0-7 7c0 5 7 13 7 13s7-8 7-13a7 7 0 0 0-7-7zm0 9.5A2.5 2.5 0 1 1 12 6.5a2.5 2.5 0 0 1 0 5z"/></svg></li>
  </ul>
</article>

<article class="card card--greek" lang="el">
  <div class="holder">
    <p class="holder__name">ΤΖΟΝ ΣΜΙΘ<span class="holder__divider">|</span><span class="holder__role">Διευθυντής</span></p>
    <p class="holder__mobile">
      <svg width="10" height="16" viewBox="0 0 10 16"><rect x="1" y="1" width="8" height="14" rx="1.5" fill="none" stroke="var(--navy)" stroke-width="1.5"/><rect x="3.5" y="12" width="3" height="1.2" fill="var(--navy)"/></svg>
      300-200-9000
    </p>
  </div>
  <div class="brand">
    <span class="brand__square"></span>
    <span class="brand__name">Fenmoor Advisory</span>
  </div>
  <ul class="contact">
    <li class="contact__item">300-200-9000 <svg viewBox="0 0 24 24"><path d="M6.6 10.8a15.1 15.1 0 0 0 6.6 6.6l2.2-2.2c.3-.3.7-.4 1-.2 1.1.4 2.3.6 3.6.6.6 0 1 .4 1 1V20c0 .6-.4 1-1 1A17 17 0 0 1 3 4c0-.6.4-1 1-1h3.5c.6 0 1 .4 1 1 0 1.3.2 2.5.6 3.6.1.3 0 .7-.2 1z"/></svg></li>
    <li class="contact__item">info@fenmooradvisory.com <svg viewBox="0 0 24 24"><path d="M2 5h20v14H2z" fill="var(--navy)"/><path d="M2 5l10 8 10-8" fill="none" stroke="#fff" stroke-width="1.6"/></svg></li>
    <li class="contact__item">www.fenmooradvisory.com <svg viewBox="0 0 24 24"><circle cx="12" cy="12" r="10" fill="none" stroke="var(--navy)" stroke-width="1.8"/><ellipse cx="12" cy="12" rx="4" ry="10" fill="none" stroke="var(--navy)" stroke-width="1.5"/><path d="M2 12h20M4 7h16M4 17h16" stroke="var(--navy)" stroke-width="1.3"/></svg></li>
    <li class="contact__item">00 εικονική πόλη, θέση 0000 <svg viewBox="0 0 24 24"><path d="M12 2a7 7 0 0 0-7 7c0 5 7 13 7 13s7-8 7-13a7 7 0 0 0-7-7zm0 9.5A2.5 2.5 0 1 1 12 6.5a2.5 2.5 0 0 1 0 5z"/></svg></li>
  </ul>
</article>

</body>
</html>
```